FC Morlan - Creation of a AD banner for our yearly event

We are a local soccer club in Switzerland. We're organizing a event that will substitute to our yearly club dinner. We need a banner AD to promote on the social networks this event.
We would like to see design that use one or the 2 colors of the club (blue and red).
This Ad should link to a online shop where we can buy vouchers.

Requirements
Must have
• Logo of the club
Title : Fête des lanternes d'hiver
Call to action : Plus d'informations
Side texte : Grande Tombola
Banner size : W300xH250 or W300xH600
Nice to have
• Promotion texte: Soutenez le FC Morlan et les restaurateurs locaux

```html
<!DOCTYPE html>
<html lang="fr">
<head>
<meta charset="utf-8">
<title>FC Morlan – Fête des lanternes d'hiver – bannières</title>
<link rel="stylesheet" href="https://fonts.googleapis.com/css2?family=Manrope:wght@500;700&family=Barlow+Semi+Condensed:wght@500;600&display=swap">
<style>
  :root {
    --club-red: #e5173f;
    --club-blue: #0a80c6;
    --white: #ffffff;
    --night-1: #1a2027;
    --night-2: #2f3a44;
    --amber: rgba(196,140,60,0.75);
    --amber-soft: rgba(168,119,46,0.45);
    --glass: rgba(170,180,188,0.28);
    --page: #ffffff;
  }
  * { box-sizing: border-box; margin: 0; padding: 0; }
  html, body {
    width: 1200px; height: 948px; overflow: hidden;
    background: var(--page);
  }
  .banner {
    position: absolute; overflow: hidden; color: var(--white);
    font-family: "Manrope", Arial, sans-serif;
  }
  .banner--rectangle { left: 15px; top: 234px; width: 511px; height: 426px; }
  .banner--skyscraper { left: 731px; top: 14px; width: 456px; height: 912px; }

  .banner__photo { position: absolute; inset: 0; }
  .banner--rectangle .banner__photo {
    background:
      radial-gradient(ellipse 70px 45px at 345px 140px, var(--amber) 0%, rgba(196,140,60,0) 100%),
      radial-gradient(ellipse 80px 50px at 420px 165px, var(--amber) 0%, rgba(196,140,60,0) 100%),
      radial-gradient(ellipse 90px 150px at 360px 90px, var(--glass) 0%, rgba(170,180,188,0) 100%),
      radial-gradient(ellipse 90px 160px at 430px 120px, var(--glass) 0%, rgba(170,180,188,0) 100%),
      linear-gradient(90deg, rgba(0,0,0,0) 88%, rgba(8,10,12,0.7) 94%, rgba(0,0,0,0) 100%),
      radial-gradient(ellipse 260px 80px at 120px 400px, rgba(150,120,90,0.35) 0%, rgba(150,120,90,0) 100%),
      linear-gradient(180deg, var(--night-2) 0%, #28323b 55%, #15191d 100%);
  }
  .banner--skyscraper .banner__photo {
    background:
      radial-gradient(ellipse 80px 60px at 240px 575px, var(--amber) 0%, rgba(196,140,60,0) 100%),
      radial-gradient(ellipse 90px 65px at 360px 625px, var(--amber) 0%, rgba(196,140,60,0) 100%),
      radial-gradient(ellipse 100px 200px at 235px 530px, var(--glass) 0%, rgba(170,180,188,0) 100%),
      radial-gradient(ellipse 110px 210px at 355px 570px, var(--glass) 0%, rgba(170,180,188,0) 100%),
      radial-gradient(ellipse 70px 320px at 420px 560px, rgba(6,8,10,0.75) 0%, rgba(6,8,10,0) 100%),
      radial-gradient(ellipse 200px 120px at 90px 790px, rgba(170,150,125,0.35) 0%, rgba(170,150,125,0) 100%),
      radial-gradient(ellipse 260px 140px at 230px 420px, var(--amber-soft) 0%, rgba(168,119,46,0) 100%),
      linear-gradient(180deg, #151b21 0%, var(--night-2) 40%, #262f37 70%, var(--night-1) 100%);
  }

  .club-mark {
    position: absolute; display: flex; flex-direction: column; align-items: center; gap: 8px;
    transform: translateX(-50%);
  }
  .club-mark__name {
    font-family: "Barlow Semi Condensed", Arial, sans-serif;
    font-weight: 600; font-size: 28px; line-height: 1; color: var(--white);
    white-space: nowrap;
  }
  .club-mark__dot {
    width: 100px; height: 100px; border-radius: 50%;
    background: var(--club-blue); border: 7px solid var(--club-red);
  }
  .banner--rectangle .club-mark { left: 131px; top: 14px; }
  .banner--skyscraper .club-mark { left: 228px; top: 28px; }
  .banner--skyscraper .club-mark__name { font-size: 32px; }
  .banner--skyscraper .club-mark__dot { width: 112px; height: 112px; }

  .title {
    position: absolute; text-align: center; font-weight: 500;
    letter-spacing: -0.2px; transform: translateX(-50%); white-space: nowrap;
  }
  .banner--rectangle .title { left: 146px; top: 172px; font-size: 34px; line-height: 44px; }
  .banner--skyscraper .title { left: 228px; top: 196px; font-size: 42px; line-height: 50px; }

  .cta {
    position: absolute; display: flex; align-items: center; justify-content: center;
    background: var(--club-red); color: var(--white);
    font-family: "Barlow Semi Condensed", Arial, sans-serif; font-weight: 500;
    font-size: 22px; text-decoration: none;
  }
  .banner--rectangle .cta { left: 20px; top: 283px; width: 260px; height: 50px; }
  .banner--skyscraper .cta { left: 96px; top: 316px; width: 260px; height: 49px; }

  .raffle { position: absolute; width: 152px; height: 152px; }
  .raffle svg { position: absolute; inset: 0; width: 100%; height: 100%; }
  .raffle__label {
    position: absolute; inset: 0; display: flex; align-items: center; justify-content: center;
    text-align: center; font-weight: 700; font-size: 22px; line-height: 1.2;
  }
  .banner--rectangle .raffle { left: 321px; top: 222px; }
  .banner--skyscraper .raffle { left: 149px; top: 685px; width: 158px; height: 158px; }
  .banner--skyscraper .raffle__label { font-size: 23px; }

  .tagline {
    position: absolute; left: 0; right: 0; text-align: center;
    font-family: "Barlow Semi Condensed", Arial, sans-serif; font-weight: 500;
    font-size: 20px; line-height: 24px;
  }
  .banner--rectangle .tagline { top: 385px; }
  .banner--skyscraper .tagline { top: 872px; font-size: 19px; }
</style>
</head>
<body>

<section class="banner banner--rectangle" aria-label="Bannière 300×250">
  <div class="banner__photo" role="img" aria-label="Photo sombre de verres de vin blanc, bouteille et plat sur une table"></div>
  <div class="club-mark">
    <span class="club-mark__name">FC Morlan</span>
    <span class="club-mark__dot"></span>
  </div>
  <h1 class="title">Fête des<br>lanternes d'hiver</h1>
  <a class="cta" href="#">Plus d'informations</a>
  <div class="raffle">
    <svg viewBox="0 0 152 152" aria-hidden="true">
      <circle cx="76" cy="76" r="74" fill="var(--club-red)"/>
      <circle cx="76" cy="76" r="66" fill="none" stroke="var(--white)" stroke-width="5" stroke-linecap="round" stroke-dasharray="0 11.5"/>
      <circle cx="76" cy="76" r="58" fill="var(--club-blue)" stroke="var(--white)" stroke-width="3"/>
    </svg>
    <div class="raffle__label">Grande<br>Tombola</div>
  </div>
  <p class="tagline">Soutenez le FC Morlan et les restaurateurs locaux</p>
</section>

<section class="banner banner--skyscraper" aria-label="Bannière 300×600">
  <div class="banner__photo" role="img" aria-label="Photo sombre de verres de vin blanc, bouteille et plat sur une table"></div>
  <div class="club-mark">
    <span class="club-mark__name">FC Morlan</span>
    <span class="club-mark__dot"></span>
  </div>
  <h1 class="title">Fête des<br>lanternes d'hiver</h1>
  <a class="cta" href="#">Plus d'informations</a>
  <div class="raffle">
    <svg viewBox="0 0 152 152" aria-hidden="true">
      <circle cx="76" cy="76" r="74" fill="var(--club-red)"/>
      <circle cx="76" cy="76" r="66" fill="none" stroke="var(--white)" stroke-width="5" stroke-linecap="round" stroke-dasharray="0 11.5"/>
      <circle cx="76" cy="76" r="58" fill="var(--club-blue)" stroke="var(--white)" stroke-width="3"/>
    </svg>
    <div class="raffle__label">Grande<br>Tombola</div>
  </div>
  <p class="tagline">Soutenez le FC Morlan et les restaurateurs locaux</p>
</section>

</body>
</html>
```